Broschüre für Trovimo-Coach
Sehr schnelle und professionelle Umsetzung. Die Designerin hat inhaltlich mitgedacht und die einzelnen Elemente passend und kreativ platziert. Der Kontakt war außerdem sehr nett. Sehr zu empfehlen!
Zielgruppe
Ich bin Deutschlands erster Trovimo-Coach. Ich zeige Unternehmern, Selbstständigen und Vertrieblern wie sie mit persönlichen Videobotschaften mehr Interessen und Abschlüsse generieren.
Aufgabenstellung
Es soll eine Broschüre grafisch gestaltet werden, die als eBook sowie für den Druck verwendet werden kann.
Format DIN A 4.
Bereitgestellt werden folgende Unterlagen:
(1) Texte und Grob-Struktur in der entsprechenden Reihenfolge.
(2) Die Broschüre soll sich an der Struktur des beigefügten eBooks 'Copper Lantern Drift' orientieren.
(3) Fotos, Logo und Grafikelemente sind beigefügt. Zusätzliches Bildmaterial darf eingesetzt werden.
(4) Ein 'Brand Look' mit Farben, Schriftarten und Stil-Elementen ist beigefügt.
(5) Druckvorlage gemäß beigefügter Vorlage von Papyrano. Für den Druck müssen es 20 oder 24 Seiten sein.
Bitte grafisch an meiner Website orientieren: www.haraldkunzo.de

```html
<!DOCTYPE html>
<html lang="de">
<head>
<meta charset="utf-8">
<title>Trovimo – Inhalt</title>
<link href="https://fonts.googleapis.com/css2?family=Poppins:wght@400;500;600;700&display=swap" rel="stylesheet">
<style>
  :root{
    --backdrop:#dedede;
    --paper:#f8f8f8;
    --ink:#1c1c2b;
    --ink-soft:#2a2a3a;
    --rule:#9fe0b4;
    --photo-top:#c9b9c3;
    --photo-mid:#d9cccb;
    --photo-bottom:#ebe2da;
    --photo-shirt:#c3d2ea;
    --photo-stage:#e9d48e;
    --photo-denim:#6c86ad;
  }
  *{box-sizing:border-box;margin:0;padding:0}
  html,body{width:1200px;height:1200px;overflow:hidden}
  body{background:var(--backdrop);font-family:"Poppins",sans-serif;color:var(--ink);position:relative}
  .spread{position:absolute;left:50px;top:180px;width:1100px;height:840px;display:flex;box-shadow:0 18px 40px rgba(0,0,0,.12)}
  .page{position:relative;width:550px;height:840px;background:var(--paper);overflow:hidden}
  .page--photo .photo{
    position:absolute;inset:0;
    background:
      radial-gradient(ellipse 260px 200px at 300px 150px, rgba(233,212,142,.55), rgba(233,212,142,0) 70%),
      radial-gradient(ellipse 220px 300px at 300px 480px, rgba(195,210,234,.85), rgba(195,210,234,0) 75%),
      radial-gradient(ellipse 150px 180px at 300px 780px, rgba(108,134,173,.55), rgba(108,134,173,0) 75%),
      linear-gradient(180deg,var(--photo-top) 0%,var(--photo-mid) 55%,var(--photo-bottom) 100%);
  }
  .running-head{position:absolute;top:28px;right:30px;display:flex;align-items:center;font-size:10px;color:var(--ink-soft)}
  .running-head .url{font-weight:500;padding-right:10px;border-right:1px solid var(--ink-soft)}
  .running-head .folio{padding-left:10px}
  .toc-title{position:absolute;left:74px;top:108px;font-size:37px;font-weight:700;letter-spacing:-.5px}
  .toc{position:absolute;left:80px;width:400px;top:0;height:100%}
  .toc-row{position:absolute;left:0;right:0;display:flex;justify-content:space-between;align-items:flex-end;font-size:13px}
  .toc-head{font-weight:600}
  .toc-col-label{font-weight:600;justify-content:flex-end}
  .toc-sub{left:34px;border-bottom:1px solid var(--rule);padding-bottom:1px;line-height:1.35}
  .toc-num{font-weight:600;font-size:12.5px}
  .toc-num--light{font-weight:400}
  .toc-plain{font-weight:400}
</style>
</head>
<body>
  <div class="spread">
    <section class="page page--photo">
      <div class="photo" role="img" aria-label="Foto: der Coach auf einer Bühne, winkend, in hellblauem Hemd und Jeans, vor unscharfem Veranstaltungshintergrund"></div>
    </section>
    <section class="page page--contents">
      <header class="running-head"><span class="url">www.haraldkunzo.de</span><span class="folio">01</span></header>
      <h1 class="toc-title">Inhalt</h1>
      <div class="toc">
        <div class="toc-row toc-col-label" style="top:168px"><span>Seite</span></div>
        <div class="toc-row toc-head" style="top:186px"><span>1. Problemanalyse</span></div>
        <div class="toc-row toc-sub" style="top:211px"><span>Ursachen</span><span class="toc-num">02</span></div>
        <div class="toc-row toc-sub" style="top:233px"><span>Zusammenfassung</span><span class="toc-num">03</span></div>
        <div class="toc-row toc-head" style="top:258px"><span>2. Trovimo – eine kurze Einführung</span></div>
        <div class="toc-row toc-sub" style="top:286px"><span>Was ist Trovimo?</span><span class="toc-num">04</span></div>
        <div class="toc-row toc-sub" style="top:310px"><span>Gründe für eine schlechte Performance<br>im Online-Vertrieb</span><span class="toc-num">05</span></div>
        <div class="toc-row toc-sub" style="top:352px"><span>Die 5 Elemente Deiner Trovimo-Strategie</span><span class="toc-num toc-num--light">06</span></div>
        <div class="toc-row toc-head" style="top:385px"><span>3. Umsetzung Deiner Trovimo-Strategie</span></div>
        <div class="toc-row toc-sub" style="top:417px"><span>Kundenreise und Video-Skripte</span><span class="toc-num">07</span></div>
        <div class="toc-row toc-sub" style="top:441px"><span>Technik-Setup und Hintergrund</span><span class="toc-num">08</span></div>
        <div class="toc-row toc-sub" style="top:465px"><span>Auswahl der Videoplattform</span><span class="toc-num">10</span></div>
        <div class="toc-row toc-sub" style="top:489px"><span>Persönliches Auftreten vor der Kamera</span><span class="toc-num">12</span></div>
        <div class="toc-row toc-sub" style="top:513px"><span>Regelmäßiges TUN und Verbessern</span><span class="toc-num">13</span></div>
        <div class="toc-row toc-plain" style="top:549px"><span>Angebot: Strategie-Gespräch</span><span class="toc-num">14</span></div>
        <div class="toc-row toc-plain" style="top:586px"><span>Angebot: Trovimo-Seminare</span><span class="toc-num">15</span></div>
        <div class="toc-row toc-plain" style="top:622px"><span>Über mich</span><span class="toc-num">16</span></div>
      </div>
    </section>
  </div>
</body>
</html>
```